Snowsports equipment company needs a product catalog

Tarrow is a small snowsports company located in the mountains of Colorado and need a product catalogue for our Telemark Skis and Bindings, also some of the accessories. you can check out our products here: tarrowcarves.com - we can use the images and copy from the website. We also have a full Brand Standards pdf that is attached. go to tarrowcarves.com to see products, images, copy.

Products to include: KLV/R, KLV/3, Vorta Ski, Pelly Ski, Crossover Kit, NTN Upgrade Kit, 75mm upgrade kit, KLV Brakes, Lighter Coil Kit, Mount Glide

We have many hero images to use as well, and you will get access to our google drive folder with images to use.
I am thinking it will be a pdf we send, but may get printed as well.

Target Market(s)

Wholesale accounts, and direct retail customers.

Contact Information for Business Card

simple with use of Brand standards.

Font styles to use
Other font styles liked:
• see brand standards

Requirements
Must have
• Adhere to our brand standards, including colors, fonts, etc.

```html
<!DOCTYPE html>
<html lang="en">
<head>
<meta charset="utf-8">
<title>Tarrow Accessories Catalog Page</title>
<link rel="stylesheet" href="https://fonts.googleapis.com/css2?family=Saira:wght@700&family=Rajdhani:wght@400&display=swap">
<style>
  :root {
    --canvas: #ffffff;
    --page-dark: #0c0c0c;
    --page-mid: #3a3a3a;
    --card-white: #ffffff;
    --card-frame: #e4e4e4;
    --card-band: #e2e2e2;
    --ink: #111111;
    --glyph-grey: #8f8f8f;
  }
  * { margin: 0; padding: 0; box-sizing: border-box; }
  html, body { width: 1200px; height: 1200px; overflow: hidden; background: var(--canvas); }
  .catalog-page {
    position: absolute; left: 164px; top: 36px; width: 872px; height: 1128px;
    background:
      radial-gradient(ellipse 60% 30% at 70% 10%, #4a4a4a 0%, transparent 70%),
      radial-gradient(ellipse 50% 40% at 20% 55%, #3c3c3c 0%, transparent 70%),
      radial-gradient(ellipse 70% 30% at 60% 95%, #5a5a5a 0%, transparent 70%),
      linear-gradient(160deg, var(--page-dark) 0%, var(--page-mid) 45%, var(--page-dark) 70%, #2a2a2a 100%);
  }
  .product-card { position: absolute; width: 318px; height: 436px; background: var(--card-band); }
  .card-a { left: 80px; top: 96px; }
  .card-b { left: 474px; top: 96px; }
  .card-c { left: 80px; top: 600px; }
  .card-d { left: 474px; top: 600px; }
  .product-shot {
    position: absolute; left: 0; top: 0; width: 318px; height: 296px;
    background: var(--card-white); padding: 9px 13px;
  }
  .shot-frame {
    width: 100%; height: 100%; border: 2px solid var(--card-frame);
    display: flex; align-items: center; justify-content: center;
  }
  .shot-fill { width: 82%; height: 62%; border-radius: 6px; }
  .fill-crossover { background: radial-gradient(ellipse at center, #5d5d5d 0%, #cfcfcf 75%, #ffffff 100%); }
  .fill-ntn { background: radial-gradient(ellipse at center, #b5b5b5 0%, #e3e3e3 70%, #ffffff 100%); }
  .fill-glide { width: 62%; height: 62%; border-radius: 50%; background: radial-gradient(circle at 40% 40%, #e8953a 0%, #8a5a28 55%, #d9cfc0 100%); }
  .unknown-glyph {
    font-family: "Rajdhani", sans-serif; font-size: 190px; line-height: 1;
    color: var(--glyph-grey);
  }
  .card-label {
    position: absolute; left: 0; top: 296px; width: 318px; height: 140px;
    display: flex; flex-direction: column; align-items: center; justify-content: center;
    text-align: center; color: var(--ink);
  }
  .product-name {
    font-family: "Saira", sans-serif; font-weight: 700; font-size: 35px;
    line-height: 1.05; letter-spacing: 0.5px; text-transform: uppercase;
  }
  .product-name.two-line { font-size: 30px; line-height: 1.25; }
  .product-price {
    font-family: "Rajdhani", sans-serif; font-weight: 400; font-size: 25px;
    margin-top: 10px; letter-spacing: -0.3px;
  }
  .two-line + .product-price { margin-top: 0; }
</style>
</head>
<body>
  <main class="catalog-page" role="img" aria-label="Black background with flowing silver smoke-like waves">
    <article class="product-card card-a">
      <div class="product-shot"><div class="shot-frame">
        <div class="shot-fill fill-crossover" role="img" aria-label="Crossover Kit parts: two black plates, two toe loops and screws"></div>
      </div></div>
      <div class="card-label">
        <h2 class="product-name">Crossover Kit</h2>
        <p class="product-price">PRICE:$499.00 USD</p>
      </div>
    </article>

    <article class="product-card card-b">
      <div class="product-shot"><div class="shot-frame">
        <div class="shot-fill fill-ntn" role="img" aria-label="NTN Upgrade Kit parts: two silver metal brackets and screws"></div>
      </div></div>
      <div class="card-label">
        <h2 class="product-name two-line">NTN Upgrade<br>Kit</h2>
        <p class="product-price">PRICE:$499.00 USD</p>
      </div>
    </article>

    <article class="product-card card-c">
      <div class="product-shot"><div class="shot-frame">
        <span class="unknown-glyph">?</span>
      </div></div>
      <div class="card-label">
        <h2 class="product-name two-line">75mm Upgrade<br>Kit</h2>
        <p class="product-price">PRICE:$749.00 USD</p>
      </div>
    </article>

    <article class="product-card card-d">
      <div class="product-shot"><div class="shot-frame">
        <div class="fill-glide" role="img" aria-label="Open tin of amber Mount Glide binding grease with labeled lid"></div>
      </div></div>
      <div class="card-label">
        <h2 class="product-name">Mount Glide</h2>
        <p class="product-price">PRICE:$10.00 USD</p>
      </div>
    </article>
  </main>
</body>
</html>
```